Kessa Lane Website Design

Need a website for a Dog Grooiming business. Please make it simular to these:

https://www.quorvatt.com
https://lintrevask.com
https://morvelandistel.com
https://www.pelthuvra.com/tensik/

```html
<!DOCTYPE html>
<html lang="en">
<head>
<meta charset="utf-8">
<title>Kessa Lane — Mobile Dog Grooming</title>
<link rel="stylesheet" href="https://fonts.googleapis.com/css2?family=Poppins:ital,wght@0,400;0,500;0,600;0,700;0,800;0,900;1,400&display=swap">
<style>
:root{
  --green:#3fcf6c;
  --green-dark:#2fb85a;
  --green-light:#5fdc82;
  --cyan:#2cc3df;
  --cyan-dark:#22aee0;
  --ink:#111111;
  --text:#555b60;
  --muted:#8a8f94;
  --about-bg:#eaf7fb;
  --white:#ffffff;
  --black:#0b0b0b;
}
*{box-sizing:border-box;margin:0;padding:0}
html,body{width:1200px;height:4415px;overflow:hidden}
body{position:relative;font-family:'Poppins',sans-serif;color:var(--ink);background:var(--white)}
.abs{position:absolute}
.ph{position:absolute}
.btn{position:absolute;display:flex;align-items:center;justify-content:center;border-radius:40px;color:#fff;font-weight:600;font-size:13px;letter-spacing:.3px;background:linear-gradient(90deg,var(--cyan),var(--green-light))}

/* header */
.site-header{position:absolute;left:0;top:0;width:1200px;height:68px;background:rgba(255,255,255,.9);z-index:5}
.brand{position:absolute;left:58px;top:16px;font-size:28px;font-weight:700}
.nav{position:absolute;left:316px;top:20px;display:flex;gap:0;font-size:11.5px}
.nav a{color:var(--ink);text-decoration:none;padding:6px 11px;border-radius:20px}
.nav a.active{background:linear-gradient(90deg,var(--cyan),var(--green-light));color:#fff;padding:6px 16px;margin-right:4px}
.call-icon{position:absolute;left:785px;top:14px;width:40px;height:40px;border-radius:50%;background:var(--cyan);display:flex;align-items:center;justify-content:center}
.call-text{position:absolute;left:838px;top:16px;font-size:10.5px;line-height:1.2}
.call-text strong{display:block;font-size:17px;font-weight:500}

/* hero */
.hero-photo{left:0;top:0;width:1200px;height:720px;background:linear-gradient(100deg,#b7a78e 0%,#d8cbb4 30%,#e7d9c4 45%,#a36a45 60%,#6f3f7a 78%,#4a2a55 100%)}
.hero-eyebrow{left:98px;top:240px;font-size:20px;color:#222}
.hero-title{left:96px;top:275px;font-size:46px;font-weight:900;line-height:52px;color:#111}
.hero-title span{color:var(--green)}
.hero-arrow{position:absolute;width:40px;height:40px;border-radius:50%;background:#fff;display:flex;align-items:center;justify-content:center}

/* appointment */
.appointment{left:0;top:690px;width:1200px;height:410px}
.appt-title{left:0;width:1200px;top:788px;text-align:center;font-size:34px;font-weight:600;color:#fff}
.appt-sub{left:360px;width:480px;top:840px;text-align:center;font-size:13.5px;line-height:22px;color:#fff}
.appt-phone{left:0;width:1200px;top:900px;text-align:center;font-size:19px;font-weight:500;color:#fff}
.appt-phone u{font-weight:600}
.pill{position:absolute;height:38px;border-radius:30px;background:var(--cyan);color:#fff;font-size:15px;font-weight:500;display:flex;align-items:center;justify-content:center;gap:10px}

/* services */
.eyebrow{position:absolute;left:0;width:1200px;text-align:center;font-size:14px;color:var(--green-dark)}
.section-title{position:absolute;left:0;width:1200px;text-align:center;font-size:36px;font-weight:700}
.section-lead{position:absolute;left:320px;width:560px;text-align:center;font-size:12px;line-height:21px;color:var(--muted)}
.service-label{position:absolute;font-size:15px;font-weight:600;line-height:20px}
.service-label.left{text-align:right;width:160px}
.service-thumb{position:absolute;width:74px;height:74px;border-radius:50%}

/* about */
.about{left:0;top:1720px;width:1200px;height:525px;background:var(--about-bg)}
.about-video{left:150px;top:1912px;width:472px;height:258px;border-radius:16px;background:linear-gradient(180deg,#8fb7d9 0%,#6e8f5c 45%,#4d7a33 100%)}
.play{position:absolute;left:348px;top:2006px;width:70px;height:70px;border-radius:50%;border:3px solid #fff;display:flex;align-items:center;justify-content:center}
.about-copy{left:687px;top:1823px;width:354px}
.about-copy .eyebrow-l{font-size:14px;color:var(--green-dark)}
.about-copy h2{font-size:36px;font-weight:700;line-height:48px}
.about-copy .lead{font-size:12px;font-weight:600;line-height:20px;margin-top:12px}
.about-copy p{font-size:11.5px;line-height:20px;color:var(--muted);margin-top:14px}

/* testimonials */
.testimonials{left:0;top:2245px;width:1200px;height:472px;background:linear-gradient(90deg,#4bcf73 0%,#5fd882 45%,#3fc86a 100%)}
.avatar{position:absolute;border-radius:50%;border:3px solid #fff}
.quote-text{left:360px;width:480px;top:2535px;text-align:center;font-size:12.5px;font-style:italic;line-height:21px;color:#fff}
.client{left:0;width:1200px;top:2622px;text-align:center;font-size:14px;font-weight:600;color:#fff}
.t-arrow{position:absolute;width:40px;height:40px;border-radius:50%;border:1.5px solid #fff;display:flex;align-items:center;justify-content:center}

/* social */
.tile{position:absolute;width:315px}
.tile.photo{height:316px}
.tile.photo .tag{position:absolute;left:14px;font-size:16px;font-weight:600;color:#fff}
.tile.photo .tag i{font-style:normal;display:inline-block;width:26px;height:26px;border:2px solid #fff;border-radius:7px;vertical-align:middle;margin-right:6px}
.tile.post{height:234px;border:1.5px solid #e6e6e6;background:#fff;padding:46px 30px 0 34px}
.post h4{font-size:15px;font-weight:500;color:var(--cyan-dark)}
.post p{font-size:11.5px;line-height:19px;color:#444;margin-top:12px}
.post a{display:block;font-size:11px;color:var(--cyan-dark);margin-top:12px;text-decoration:none}

/* press */
.press{position:absolute;top:3955px;width:158px;height:74px;border:1.5px solid #e3e3e3;display:flex;align-items:center;justify-content:center;font-size:26px;font-weight:600;color:#111}

/* newsletter */
.newsletter{left:0;top:4102px;width:1200px;height:76px;background:var(--green)}
.news-title{left:213px;top:4123px;font-size:22px;font-weight:600;color:#fff}
.news-field{left:568px;top:4121px;width:440px;height:38px;border-radius:30px;background:#fff;border:2px solid #dff5e6}
.news-field span{position:absolute;left:20px;top:11px;font-size:11px;color:#555}
.news-field b{position:absolute;right:2px;top:2px;width:112px;height:30px;border-radius:30px;background:linear-gradient(90deg,var(--cyan),var(--green-light));color:#fff;font-size:12px;display:flex;align-items:center;justify-content:center}

/* footer */
.footer{left:0;top:4178px;width:1200px;height:237px;background:var(--black);color:#fff}
.f-brand{left:58px;top:4235px;font-size:38px;font-weight:700;color:#fff}
.f-tag{left:60px;top:4294px;font-size:13.5px;color:#fff}
.f-phone{left:62px;top:4320px;font-size:19px;font-weight:500;color:var(--green)}
.f-phone u{color:var(--cyan)}
.f-social{position:absolute;top:4262px;width:38px;height:38px;border-radius:50%;background:var(--green)}
.f-nav{left:700px;width:440px;top:4302px;text-align:right;font-size:11px;color:#fff;word-spacing:2px}
.f-copy{left:700px;width:440px;top:4326px;text-align:right;font-size:11px;color:#fff}
.f-copy span{color:var(--cyan)}
</style>
</head>
<body>

<!-- HERO -->
<div class="ph hero-photo" role="img" aria-label="Photo of a smiling groomer in an apron holding a phone beside a small fluffy dog on a grooming table"></div>
<header class="site-header">
  <div class="brand">Kessa Lane</div>
  <nav class="nav">
    <a class="active">Home</a><a>About</a><a>Services</a><a>Careers</a><a>Blog</a><a>Faq's</a><a>Contact Us</a>
  </nav>
  <div class="call-icon"><svg width="20" height="20" viewBox="0 0 24 24"><path fill="#fff" d="M6.6 10.8a15.1 15.1 0 0 0 6.6 6.6l2.2-2.2a1 1 0 0 1 1-.25 11.4 11.4 0 0 0 3.6.57 1 1 0 0 1 1 1V20a1 1 0 0 1-1 1A17 17 0 0 1 3 4a1 1 0 0 1 1-1h3.5a1 1 0 0 1 1 1c0 1.25.2 2.45.57 3.57a1 1 0 0 1-.25 1z"/></svg></div>
  <div class="call-text">Call Us On:<strong>+1 000 000 0000</strong></div>
  <div class="btn" style="left:994px;top:14px;width:146px;height:40px;font-size:14px">BOOK ONLINE</div>
</header>
<div class="abs hero-eyebrow">We Keep Them Happy Anytime.</div>
<h1 class="abs hero-title">Happy Mobile<br><span>Dog Grooming</span><br>Services</h1>
<div class="btn" style="left:98px;top:443px;width:146px;height:38px">BOOK ONLINE</div>
<div class="hero-arrow" style="left:40px;top:345px"><svg width="12" height="14" viewBox="0 0 12 14"><path d="M8 2 3 7l5 5" stroke="#222" stroke-width="2" fill="none"/></svg></div>
<div class="hero-arrow" style="left:1122px;top:345px"><svg width="12" height="14" viewBox="0 0 12 14"><path d="m4 2 5 5-5 5" stroke="#222" stroke-width="2" fill="none"/></svg></div>

<!-- APPOINTMENT -->
<svg class="abs appointment" viewBox="0 0 1200 410" preserveAspectRatio="none" aria-hidden="true">
  <defs><linearGradient id="apg" x1="0" y1="0" x2="0" y2="1"><stop offset="0" stop-color="#46d873"/><stop offset="1" stop-color="#2fb85a"/></linearGradient></defs>
  <path d="M0 22 C200 -10 380 40 600 24 C820 8 1000 -8 1200 22 L1200 360 C1000 400 800 360 600 380 C380 400 180 360 0 395 Z" fill="url(#apg)"/>
</svg>
<div class="abs appt-title">Make An Appointment !</div>
<div class="abs appt-sub">Every Kessa Lane Signature Service is one-on-one with a gentle &amp; compassionate expert groomer</div>
<div class="abs appt-phone">+1 000 000 0000 &nbsp;or&nbsp; <u>BOOK ONLINE</u></div>
<div class="pill" style="left:475px;top:959px;width:120px">
  <svg width="18" height="18" viewBox="0 0 24 24"><path fill="#fff" d="M6.6 10.8a15.1 15.1 0 0 0 6.6 6.6l2.2-2.2a1 1 0 0 1 1-.25 11.4 11.4 0 0 0 3.6.57 1 1 0 0 1 1 1V20a1 1 0 0 1-1 1A17 17 0 0 1 3 4a1 1 0 0 1 1-1h3.5a1 1 0 0 1 1 1c0 1.25.2 2.45.57 3.57a1 1 0 0 1-.25 1z"/></svg>CALL</div>
<div class="pill" style="left:605px;top:959px;width:120px">
  <svg width="20" height="18" viewBox="0 0 24 22"><path fill="#fff" d="M3 3h14a2 2 0 0 1 2 2v8a2 2 0 0 1-2 2H9l-5 4v-4H3a2 2 0 0 1-2-2V5a2 2 0 0 1 2-2z"/></svg>TEXT</div>
<div class="ph" style="left:960px;top:785px;width:175px;height:305px;border-radius:80px 80px 30px 30px;background:linear-gradient(180deg,#8a5a3a,#5e3a22)" role="img" aria-label="Photo of a curly brown doodle dog sitting"></div>

<!-- SERVICES -->
<div class="eyebrow" style="top:1142px">What We Do</div>
<h2 class="section-title" style="top:1162px">Our Services</h2>
<p class="section-lead" style="top:1222px">Lorem Ipsum is simply dummy text of the printing typesetting industry. Lorem Ipsum has been the industry's standard text ever since the, when an unknown printer.</p>
<svg class="abs" style="left:0;top:1300px" width="1200" height="350" aria-hidden="true">
  <path d="M360 18 C300 110 280 240 360 330" stroke="#333" stroke-width="1" stroke-dasharray="3 4" fill="none"/>
  <path d="M828 18 C900 110 920 240 828 330" stroke="#333" stroke-width="1" stroke-dasharray="3 4" fill="none"/>
  <circle cx="360" cy="18" r="3" fill="#111"/><circle cx="360" cy="330" r="3" fill="#111"/>
  <circle cx="828" cy="18" r="3" fill="#111"/><circle cx="828" cy="330" r="3" fill="#111"/>
</svg>
<div class="ph" style="left:405px;top:1330px;width:385px;height:290px;border-radius:40px;background:linear-gradient(90deg,#c98a3e,#2f63c8 45%,#2a5ab8 75%,#c07f3a)" role="img" aria-label="Photo of a golden retriever wearing a blue drying robe"></div>

<div class="service-label left" style="left:110px;top:1330px">Warm Filtered<br>Water Bath</div>
<div class="service-thumb" style="left:283px;top:1318px;background:#d9cdbd" role="img" aria-label="Dog being bathed"></div>
<div class="service-label left" style="left:58px;top:1447px">All Natural<br>Products</div>
<div class="service-thumb" style="left:232px;top:1434px;background:#9a8a70" role="img" aria-label="Grooming product bottles"></div>
<div class="service-label left" style="left:110px;top:1573px">Gentle Brush<br>&amp; Blowout</div>
<div class="service-thumb" style="left:283px;top:1556px;background:#8b5a3a" role="img" aria-label="Dog being brushed"></div>

<div class="service-thumb" style="left:830px;top:1318px;background:#c8a070" role="img" aria-label="Dog nails being trimmed"></div>
<div class="service-label" style="left:922px;top:1330px">Trim &amp; File<br>Nails</div>
<div class="service-thumb" style="left:882px;top:1434px;background:#5bbd5e" role="img" aria-label="Dog with clean teeth"></div>
<div class="service-label" style="left:970px;top:1447px">Clean Teeth<br>&amp; Ears</div>
<div class="service-thumb" style="left:830px;top:1556px;background:#d8b090" role="img" aria-label="Small dog after breed specific groom"></div>
<div class="service-label" style="left:927px;top:1573px">Breed Specific<br>Pro Groom</div>

<!-- ABOUT -->
<svg class="abs about" viewBox="0 0 1200 525" preserveAspectRatio="none" aria-hidden="true">
  <path d="M0 20 C200 -5 400 30 600 12 C800 -6 1000 28 1200 10 L1200 525 L0 525 Z" fill="#eaf7fb"/>
</svg>
<div class="ph about-video" role="img" aria-label="Video still of a dog lying on a lawn in front of a brick house"></div>
<div class="play"><svg width="24" height="28" viewBox="0 0 24 28"><path d="M3 2v24l19-12z" fill="#fff"/></svg></div>
<div class="abs about-copy">
  <div class="eyebrow-l">About</div>
  <h2>Kessa Lane</h2>
  <div class="lead">Lorem Ipsum is simply dummy text of the printing and typesetting industry has been the industry.</div>
  <p>Lorem Ipsum is simply dummy text of the printing typesetting industry. Lorem Ipsum has been the industry's standard text ever since the 1500s, when an unknown printer.</p>
  <p>Lorem Ipsum is simply dummy text of the printing typesetting industry. Lorem Ipsum has been the industry's standard text ever since the 1500s, when an unknown printer took a galley type and scrambled it to make a type specimen book.</p>
</div>
<div class="btn" style="left:687px;top:2132px;width:142px;height:38px">LEARN MORE</div>

<!-- TESTIMONIALS -->
<div class="ph testimonials" role="img" aria-label="Photo of a girl hugging a happy golden dog on grass under a green tint"></div>
<div class="abs" style="left:0;width:1200px;top:2316px;text-align:center;font-size:14px;color:#111">Testimonials</div>
<h2 class="section-title" style="top:2338px;color:#fff">What Our Client Say</h2>
<div class="avatar" style="left:493px;top:2405px;width:58px;height:58px;background:#bdbdbd" role="img" aria-label="Client photo"></div>
<div class="avatar" style="left:565px;top:2398px;width:72px;height:72px;background:#d7b7a0" role="img" aria-label="Client photo"></div>
<div class="avatar" style="left:651px;top:2405px;width:58px;height:58px;background:#9a9a9a" role="img" aria-label="Client photo"></div>
<svg class="abs" style="left:578px;top:2485px" width="44" height="34" viewBox="0 0 44 34" aria-hidden="true"><path d="M2 2h16v16c0 8-5 14-13 15l-1-4c5-1 7-5 7-9H2zM26 2h16v16c0 8-5 14-13 15l-1-4c5-1 7-5 7-9h-9z" fill="#111"/></svg>
<p class="abs quote-text">Lorem ipsum has been the industry's standard dummy text ever since the 1500s, when an unknown printer took a galley of type and scrambled it to make a type specimen book.</p>
<div class="abs client">— &nbsp;CLIENT NAME</div>
<div class="t-arrow" style="left:181px;top:2447px"><svg width="12" height="14" viewBox="0 0 12 14"><path d="M8 2 3 7l5 5" stroke="#fff" stroke-width="2" fill="none"/></svg></div>
<div class="t-arrow" style="left:959px;top:2447px"><svg width="12" height="14" viewBox="0 0 12 14"><path d="m4 2 5 5-5 5" stroke="#fff" stroke-width="2" fill="none"/></svg></div>

<!-- SOCIAL -->
<h2 class="section-title" style="top:2788px;line-height:42px">Now We Are<br>Social</h2>

<div class="tile photo" style="left:113px;top:2910px;background:linear-gradient(135deg,#d9b58f,#b56a35)" role="img" aria-label="Photo of a spaniel being combed"><div class="tag" style="top:14px"><i></i># Happy Dog</div></div>
<div class="tile post" style="left:443px;top:2910px"><h4>@Dog Grooiming | 20 Sep</h4><p>" Lorem Ipsum has been the industry standard dummy text ever since the when an unknown printer took a galley of type and scrambled "</p><a>https://kessalane-care.com</a></div>
<div class="tile photo" style="left:772px;top:2910px;background:linear-gradient(180deg,#e8e8e8,#8c8c8c)" role="img" aria-label="Photo of a small dog in a bath with bubbles"><div style="position:absolute;left:0;bottom:0;width:100%;height:90px;background:rgba(60,60,60,.55)"></div><div class="tag" style="top:248px"># Happy Dog<br><span style="font-size:11px;font-weight:400;color:var(--cyan)">https://kessalane-care.com</span></div></div>

<div class="tile post" style="left:113px;top:3243px"><h4>@Dog Grooiming | 20 Sep</h4><p>" Lorem Ipsum has been the industry standard dummy text ever since the when an unknown printer took a galley of type and scrambled "</p><a>https://kessalane-care.com</a></div>
<div class="tile photo" style="left:443px;top:3161px;background:linear-gradient(135deg,#c9b48e,#5d6b7c)" role="img" aria-label="Photo of a woman hugging a husky outdoors"><div class="tag" style="top:270px"><i></i># Happy Dog</div></div>
<div class="tile post" style="left:772px;top:3243px"><h4>@Dog Grooiming | 20 Sep</h4><p>" Lorem Ipsum has been the industry standard dummy text ever since the when an unknown printer took a galley of type and scrambled "</p><a>https://kessalane-care.com</a></div>

<div class="tile photo" style="left:113px;top:3491px;background:linear-gradient(135deg,#d08a4a,#2a2a2a)" role="img" aria-label="Photo of a man grooming a white fluffy dog"><div class="tag" style="top:14px"><i></i># Happy Dog</div></div>
<div class="tile post" style="left:443px;top:3491px"><h4>@Dog Grooiming | 20 Sep</h4><p>" Lorem Ipsum has been the industry standard dummy text ever since the when an unknown printer took a galley of type and scrambled "</p><a>https://kessalane-care.com</a></div>
<div class="tile photo" style="left:772px;top:3491px;background:linear-gradient(180deg,#2f3a22,#6f7e3a)" role="img" aria-label="Photo of a dog running across a field"><div class="tag" style="top:14px"><i></i># Happy Dog</div></div>

<!-- AS SEEN IN -->
<h3 class="abs" style="left:0;width:1200px;top:3893px;text-align:center;font-size:26px;font-weight:500">As Seen In</h3>
<div class="press" style="left:178px">Halvern</div>
<div class="press" style="left:350px">Tovique</div>
<div class="press" style="left:521px">Brindell</div>
<div class="press" style="left:693px">Marosk</div>
<div class="press" style="left:865px">Quen</div>

<!-- NEWSLETTER -->
<div class="abs newsletter"></div>
<div class="abs news-title">Subscribe To Our Newsletter</div>
<div class="abs news-field"><span>Enter Email *</span><b>SUBSCRIBE</b></div>

<!-- FOOTER -->
<footer class="abs footer"></footer>
<div class="abs f-brand">Kessa Lane</div>
<div class="abs f-tag">Doorstep Dog Grooming</div>
<div class="abs f-phone">+1 000 000 0000 &nbsp;<span style="color:#fff">or</span>&nbsp; <u>BOOK ONLINE</u></div>
<div class="f-social" style="left:958px" aria-label="Social link"></div>
<div class="f-social" style="left:1005px" aria-label="Social link"></div>
<div class="f-social" style="left:1052px" aria-label="Social link"></div>
<div class="f-social" style="left:1099px" aria-label="Social link"></div>
<div class="abs f-nav">Home &nbsp;|&nbsp; About &nbsp;|&nbsp; Services &nbsp;|&nbsp; Careers &nbsp;|&nbsp; Blog &nbsp;|&nbsp; Faq's &nbsp;|&nbsp; Contact Us</div>
<div class="abs f-copy">©<span>Kessa Lane</span> -2021 All rights reserved.</div>

</body>
</html>
```